Property development company needs a name card design

I started my company since 2010, based in Auckland, New Zealand. We have been doing residential property rentals, individual low-rise residential property construction, small to medium scale residential development project. We will be participate in property investment as well. I have no favor of any specific design or color, just be creative and do anything you think will match the concept.

```html
<!DOCTYPE html>
<html lang="en">
<head>
<meta charset="utf-8">
<title>Kowhai Investment &amp; Development – Name Card</title>
<link rel="stylesheet" href="https://fonts.googleapis.com/css2?family=Abril+Fatface&display=swap">
<style>
  :root {
    --page-bg: #e9e9e9;
    --cream: #fafaf0;
    --cream-shade: #ecebdd;
    --blue-deep: #0b4f86;
    --blue-mid: #0f74c0;
    --blue-bright: #2a9be0;
    --aqua: #2fc6dc;
    --white: #ffffff;
    --name-blue: #1678c2;
  }
  html, body {
    margin: 0;
    width: 1200px;
    height: 1000px;
    overflow: hidden;
    background: var(--page-bg);
    font-family: "Abril Fatface", "Bodoni Moda", Georgia, serif;
  }
  .canvas {
    position: relative;
    width: 1200px;
    height: 1000px;
  }
  .card {
    position: absolute;
    left: 280px;
    width: 640px;
    height: 384px;
    overflow: hidden;
    box-shadow: 0 8px 22px rgba(0,0,0,.25);
  }
  .card-front { top: 70px; background: var(--cream); }
  .card-back {
    top: 536px;
    background:
      radial-gradient(ellipse 60% 55% at 62% 60%, rgba(150,225,240,.75), transparent 70%),
      linear-gradient(170deg, var(--blue-deep) 0%, var(--blue-bright) 45%, var(--aqua) 70%, #1a9fb8 100%);
  }
  .card-art { position: absolute; inset: 0; }
  .holder-name {
    position: absolute;
    left: 0; right: 40px;
    top: 150px;
    margin: 0;
    text-align: center;
    color: var(--name-blue);
    font-size: 62px;
    font-weight: 400;
    letter-spacing: 1px;
    text-shadow: 2px 3px 3px rgba(0,0,0,.25);
  }
  .company-band {
    position: absolute;
    left: 0; right: 0; bottom: 0;
    height: 48px;
    background: linear-gradient(to bottom, var(--blue-bright), var(--blue-mid));
    border-top: 6px solid #3aa6e6;
    display: flex;
    align-items: center;
    justify-content: center;
    color: var(--white);
    font-size: 20px;
  }
  .brand {
    position: absolute;
    display: flex;
    align-items: center;
    gap: 8px;
    color: var(--white);
    font-size: 20px;
  }
  .brand-mark {
    width: 12px; height: 12px;
    background: var(--white);
  }
  .brand-corner { top: 24px; right: 26px; }
  .brand-large {
    left: 0; right: 0; top: 0; bottom: 0;
    justify-content: center;
    font-size: 64px;
    gap: 18px;
    color: rgba(255,255,255,.9);
  }
  .brand-large .brand-mark { width: 30px; height: 30px; background: rgba(255,255,255,.9); }
</style>
</head>
<body>
<main class="canvas">
  <section class="card card-front">
    <svg class="card-art" viewBox="0 0 640 384" width="640" height="384" aria-hidden="true">
      <defs>
        <linearGradient id="cornerBlue" x1="0" y1="0" x2="1" y2="1">
          <stop offset="0" stop-color="#0b4f86"/>
          <stop offset="0.5" stop-color="#157fca"/>
          <stop offset="1" stop-color="#0b5a94"/>
        </linearGradient>
      </defs>
      <rect x="0" y="0" width="640" height="14" fill="var(--cream-shade)"/>
      <path d="M340 0 Q600 10 640 290 L640 0 Z" fill="url(#cornerBlue)"/>
      <path d="M0 26 Q420 -10 560 50 Q640 120 640 300 L640 310 Q630 130 552 62 Q430 6 0 34 Z" fill="var(--cream)"/>
      <path d="M0 28 Q430 -4 556 56 Q634 124 640 304" fill="none" stroke="#5f9fcf" stroke-width="3"/>
    </svg>
    <div class="brand brand-corner"><span class="brand-mark"></span>Kowhai</div>
    <h1 class="holder-name">Mara Lindqvist</h1>
    <div class="company-band">Kowhai investment &amp; development Ltd</div>
  </section>

  <section class="card card-back">
    <div class="brand brand-large"><span class="brand-mark"></span>Kowhai</div>
  </section>
</main>
</body>
</html>
```